Business Card Design/Logo

I require a design/logo for my own Company, Morvix. The Jewellery I make is totally hand crafted. I own a hand Mining Claim out in the gemfields of Queensland and dig up my own stones. I also fossick for Gold Locally so all my Jewellery products are hand dug/cut/created. Quality stones are hand cut by my partner (Faceted) and other stones (Seconds) are either skin polished or recessed into pieces of Solid 925 Silver or Solid 9ct and 18 ct Gold. I make Sets (Collections) or just one-of designs. All the stones come in different colours and I am now starting to use different colour Golds. The final design should radiate professionalism, quality and uniqueness.

Target Market(s)

Many designs will cost a minimum of AU Dollars $2,000

Industry/Entity Type

Business

Contact Information for Business Card

Morvix Creations
Distinct Bench Wrought Native Adornments
0400327986
P.O. Box 418 Ambercrest 4719 Qld
morvixgarnets@mailbrook.net

```html
<!DOCTYPE html>
<html lang="en">
<head>
<meta charset="utf-8">
<title>Morvix Creations — Business Card</title>
<link rel="stylesheet" href="https://fonts.googleapis.com/css2?family=Arimo&family=Tinos:ital@1&display=swap">
<style>
  :root {
    --backdrop: #d6a9d9;
    --plum: #8e1467;
    --plum-deep: #6a0c4c;
    --maroon: #6b0f24;
    --maroon-deep: #4a0716;
    --gold: #f2c230;
    --gold-bright: #fbe04a;
    --gold-deep: #c8901a;
    --text-gold: #f5c21e;
  }
  html, body {
    margin: 0;
    width: 1200px;
    height: 928px;
    overflow: hidden;
    background: var(--backdrop);
  }
  .card {
    position: absolute;
    left: 75px;
    top: 164px;
    width: 1050px;
    height: 600px;
    overflow: hidden;
    box-shadow: 0 10px 30px rgba(60, 0, 50, 0.35);
  }
  .card-art {
    position: absolute;
    inset: 0;
    width: 100%;
    height: 100%;
  }
  .brand-name {
    position: absolute;
    left: 56px;
    top: 36px;
    margin: 0;
    font-family: "Arimo", Arial, sans-serif;
    font-weight: 400;
    font-size: 100px;
    line-height: 1.05;
    color: var(--text-gold);
  }
  .brand-name .brand-sub {
    display: block;
    font-size: 42px;
    line-height: 1.1;
    padding-left: 176px;
  }
  .tagline {
    position: absolute;
    left: 88px;
    top: 292px;
    margin: 0;
    font-family: "Tinos", "Times New Roman", serif;
    font-style: italic;
    font-size: 28px;
    color: var(--text-gold);
  }
  .contact {
    position: absolute;
    right: 56px;
    top: 84px;
    margin: 0;
    font-family: "Arimo", Arial, sans-serif;
    font-size: 29px;
    line-height: 1.32;
    color: var(--text-gold);
    text-align: right;
    font-style: normal;
  }
  .rings {
    position: absolute;
    left: 665px;
    top: 250px;
    width: 300px;
    height: 290px;
    border-radius: 18px;
    background: linear-gradient(160deg, rgba(242, 194, 48, 0.55), rgba(200, 144, 26, 0.35));
  }
</style>
</head>
<body>
  <div class="card">
    <svg class="card-art" viewBox="0 0 1050 600" preserveAspectRatio="none" aria-hidden="true">
      <defs>
        <linearGradient id="plumField" x1="0" y1="0" x2="1" y2="1">
          <stop offset="0" stop-color="#a01e76"/>
          <stop offset="0.6" stop-color="#8a1263"/>
          <stop offset="1" stop-color="#6e0c50"/>
        </linearGradient>
        <linearGradient id="goldBand" x1="0" y1="0" x2="0" y2="1">
          <stop offset="0" stop-color="#fbe04a"/>
          <stop offset="0.5" stop-color="#f2c230"/>
          <stop offset="1" stop-color="#c8901a"/>
        </linearGradient>
        <linearGradient id="maroonBase" x1="0" y1="0" x2="0" y2="1">
          <stop offset="0" stop-color="#7c1530"/>
          <stop offset="1" stop-color="#4a0716"/>
        </linearGradient>
      </defs>
      <rect width="1050" height="600" fill="url(#plumField)"/>
      <path d="M0 140 C250 60 520 200 1050 90 L1050 160 C560 260 260 120 0 230 Z" fill="#b23a8a" opacity="0.35"/>
      <path d="M120 0 C260 120 300 260 520 330 L420 330 C260 260 200 120 40 0 Z" fill="#6a0c4c" opacity="0.25"/>
      <path d="M0 380 C300 330 650 360 1050 250 L1050 320 C650 420 300 400 0 450 Z" fill="#b23a8a" opacity="0.35"/>
      <path d="M0 430 C320 400 680 410 1050 330 L1050 600 L0 600 Z" fill="url(#maroonBase)"/>
      <path d="M0 418 C320 385 680 395 1050 318 L1050 346 C680 425 320 415 0 446 Z" fill="url(#goldBand)"/>
      <path d="M0 480 C320 455 680 450 1050 385 L1050 396 C680 465 320 472 0 492 Z" fill="#f2c230" opacity="0.85"/>
      <path d="M0 540 C300 520 700 520 1050 470 L1050 480 C700 535 300 535 0 552 Z" fill="#f2c230" opacity="0.55"/>
    </svg>

    <h1 class="brand-name">Morvix<span class="brand-sub">Creations</span></h1>
    <p class="tagline">Distinct Bench Wrought Native Adornments</p>

    <address class="contact">
      0400327986<br>
      P.O. Box 418 Ambercrest 4719 Qld<br>
      morvixgarnets@mailbrook.net
    </address>

    <div class="rings" role="img" aria-label="Photograph of two gold gemstone rings"></div>
  </div>
</body>
</html>
```